Harbor Nightclub

Nightclub flyer., digital single sided, for KV and PX. I included samples of some previous flyers we've used. Sample Info:
HARBOR
FRIDAYS
FRI MAY 1 2020
DJ VORTAN (club floor)
DJ RUZO & DJ TAV (residents on the lounge floor)
4217 Marlow Avenue Sacramento
www.harborvenuehall.example for list/VIP inquiries

Target Market(s)

Upscale top 40 crowd but want some cool and artsy like the examples included.

Font styles to use
Sans Serif

Requirements
Must have
• Harbor Logo
Nice to have
• Would be nice if the flyer can be incorporated later with DJ photos (sometimes we will add dj photos to pixagram etc). Would like a big city type of feel.
Should not have
• Nothing too sexual.

```html
<!DOCTYPE html>
<html lang="en">
<head>
<meta charset="utf-8">
<title>Harbor Fridays</title>
<link rel="stylesheet" href="https://fonts.googleapis.com/css2?family=Exo+2:wght@500;600&family=Open+Sans:wght@600;700&display=swap">
<style>
  :root {
    --ink: #000000;
    --white: #ffffff;
    --violet: #a43bd6;
    --violet-soft: #c77be8;
    --glow: #f3e4ff;
    --smoke: #6f6a72;
  }
  html, body { margin: 0; padding: 0; overflow: hidden; background: var(--ink); }
  .flyer {
    position: relative; width: 961px; height: 1200px; overflow: hidden;
    background: var(--ink); color: var(--white);
    font-family: "Exo 2", sans-serif;
  }
  .hero-photo {
    position: absolute; left: 0; top: 0; width: 961px; height: 760px;
    background:
      radial-gradient(ellipse 300px 170px at 530px 255px, #d9d3dc 0%, #8c8590 35%, transparent 75%),
      radial-gradient(ellipse 620px 360px at 500px 320px, #3a3340 0%, #1a141e 55%, transparent 90%),
      linear-gradient(160deg, transparent 45%, rgba(164,59,214,0.35) 60%, transparent 72%);
  }
  .streaks { position: absolute; left: 0; top: 0; }
  .date {
    position: absolute; left: 24px; top: 44px; margin: 0;
    font-family: "Open Sans", sans-serif; font-weight: 600; font-size: 27px;
  }
  .title {
    position: absolute; left: 0; right: 0; top: 355px; margin: 0; text-align: center;
    font-weight: 500; font-size: 128px; letter-spacing: 2px; line-height: 1;
    color: var(--glow);
    text-shadow: 0 0 6px var(--violet-soft), 0 0 18px var(--violet), 0 0 36px var(--violet);
  }
  .club-dj {
    position: absolute; left: 0; right: 0; top: 583px; margin: 0; text-align: center;
    font-weight: 500; font-size: 36px;
  }
  .club-floor {
    position: absolute; left: 0; right: 0; top: 646px; margin: 0; text-align: center;
    font-weight: 500; font-size: 19px;
  }
  .bracket, .accent { color: var(--violet); }
  .resident-djs {
    position: absolute; left: 0; right: 0; top: 775px; margin: 0; text-align: center;
    font-weight: 500; font-size: 66px; letter-spacing: 1px; line-height: 1;
  }
  .resident-djs .slash { color: var(--violet-soft); margin: 0 22px; font-weight: 500; }
  .resident-floor {
    position: absolute; left: 0; right: 0; top: 870px; margin: 0; text-align: center;
    font-weight: 600; font-size: 35px; letter-spacing: 2px;
  }
  .address {
    position: absolute; left: 18px; top: 1083px; margin: 0;
    font-family: "Open Sans", sans-serif; font-weight: 700; font-size: 33px;
  }
  .web {
    position: absolute; left: 20px; top: 1135px; margin: 0;
    font-family: "Open Sans", sans-serif; font-weight: 600; font-size: 18px;
  }
  .venue-mark {
    position: absolute; left: 735px; top: 1035px; width: 170px; text-align: center;
  }
  .venue-mark .dot {
    display: block; width: 76px; height: 76px; margin: 0 auto 14px;
    border: 4px solid var(--white); border-radius: 50%; box-sizing: border-box;
  }
  .venue-mark .name {
    font-weight: 500; font-size: 38px; letter-spacing: 2px; color: var(--white);
  }
</style>
</head>
<body>
<main class="flyer">
  <div class="hero-photo" role="img" aria-label="Close-up photograph of a face with a purple tint, a single eye at the centre"></div>
  <svg class="streaks" width="961" height="1200" viewBox="0 0 961 1200" aria-hidden="true">
    <line x1="0" y1="905" x2="330" y2="835" stroke="#a43bd6" stroke-width="3"/>
    <line x1="0" y1="1095" x2="130" y2="1005" stroke="#a43bd6" stroke-width="5"/>
    <line x1="520" y1="945" x2="961" y2="1175" stroke="#a43bd6" stroke-width="4"/>
    <line x1="660" y1="950" x2="961" y2="1080" stroke="#7d2aa6" stroke-width="2"/>
  </svg>

  <p class="date">FRI MAY 1 2020</p>
  <h1 class="title">FRIDAYS</h1>

  <p class="club-dj">DJ VORTAN</p>
  <p class="club-floor"><span class="bracket">[</span> CLUB FLOOR <span class="bracket">]</span></p>

  <p class="resident-djs">DJ RUZO<span class="slash">/</span>DJ TAV</p>
  <p class="resident-floor"><span class="bracket">[</span> RESIDENTS ON <span class="accent">THE</span> LOUNGE FLOOR <span class="bracket">]</span></p>

  <p class="address">4217 Marlow Avenue Sacramento</p>
  <p class="web">www.harborvenuehall.example for list/VIP inquiries</p>

  <div class="venue-mark">
    <span class="dot"></span>
    <span class="name">HARBOR</span>
  </div>
</main>
</body>
</html>
```